Silver Falcon Construction Services

Create a business card for my business consulting company
Marissa Vendt, Founder and CEO
4816 Willow Crest Ave, Ste 240
Lakewood, CO. 80401
720.555.0187 cell
mvendt@silverfalconbuild.example
www.silverfalconbuild.example

Target Market(s)

Private Equity and Construction Companies

Industry/Entity Type

Business / Sales Consulting

Tag Line that says "Where Every Great Plan Begins With Solid Groundwork"

Requirements
Must have
• Logo on both sides of the card.
Nice to have
• Add tagline to the same side of the card as my name and contact info

```html
<!DOCTYPE html>
<html lang="en">
<head>
<meta charset="utf-8">
<title>Silver Falcon Construction Services – Business Card</title>
<link href="https://fonts.googleapis.com/css2?family=Montserrat:wght@400;500;700&display=swap" rel="stylesheet">
<style>
  :root {
    --stage: #3b3b3b;
    --card: #ffffff;
    --ink: #111111;
    --ink-soft: #2a2a2a;
    --band: #0d0d0d;
    --band-text: #ffffff;
  }
  * { box-sizing: border-box; margin: 0; padding: 0; }
  html, body {
    width: 1200px; height: 689px; overflow: hidden;
    background: var(--stage);
    font-family: "Montserrat", sans-serif;
    color: var(--ink);
  }
  .stage {
    position: relative; width: 1200px; height: 689px;
    display: flex; align-items: center; justify-content: center; gap: 40px;
  }
  .card {
    position: relative; width: 540px; height: 309px;
    background: var(--card); border-radius: 18px; overflow: hidden;
  }
  .band-rule {
    position: absolute; left: 0; right: 0; bottom: 48px;
    height: 2px; background: var(--band);
  }
  .band {
    position: absolute; left: 0; right: 0; bottom: 0; height: 42px;
    background: var(--band); color: var(--band-text);
    display: flex; align-items: center; justify-content: center;
    font-size: 14px; font-weight: 400; letter-spacing: 0.4px;
  }
  .wordmark {
    display: flex; align-items: center; gap: 10px;
    font-weight: 700; color: var(--ink);
  }
  .wordmark-square { width: 14px; height: 14px; background: var(--ink); flex: none; }
  .wordmark-text { display: flex; flex-direction: column; line-height: 1.05; }
  .wordmark-name { text-transform: uppercase; letter-spacing: 1px; }
  .wordmark-sub { text-transform: uppercase; letter-spacing: 2.4px; }

  /* front */
  .card-front .wordmark {
    position: absolute; left: 0; right: 0; top: 92px; justify-content: center;
  }
  .card-front .wordmark-name { font-size: 34px; }
  .card-front .wordmark-sub { font-size: 12px; margin-top: 6px; border-top: 2px solid var(--ink); padding-top: 6px; }
  .card-front .wordmark-square { width: 22px; height: 22px; }

  /* back */
  .card-back .wordmark { position: absolute; right: 30px; top: 34px; }
  .card-back .wordmark-name { font-size: 20px; }
  .card-back .wordmark-sub { font-size: 7.5px; margin-top: 4px; letter-spacing: 1.6px; }
  .logo-rule {
    position: absolute; right: 30px; top: 96px; width: 230px; height: 1.5px; background: var(--ink);
  }
  .person { position: absolute; left: 30px; top: 132px; }
  .person-name { font-size: 22px; font-weight: 700; }
  .person-title { font-size: 13px; font-weight: 400; color: var(--ink-soft); margin-top: 2px; }
  .divider {
    position: absolute; left: 30px; right: 30px; top: 186px; height: 1.5px; background: var(--ink);
  }
  .contacts { position: absolute; left: 30px; top: 196px; list-style: none; }
  .contacts li {
    display: flex; align-items: center; gap: 9px;
    font-size: 11.5px; line-height: 19px; color: var(--ink-soft);
  }
  .contacts svg { width: 12px; height: 12px; flex: none; }
  .address {
    position: absolute; right: 30px; top: 200px; text-align: right;
    font-size: 11.5px; line-height: 18px; color: var(--ink-soft); font-style: normal;
  }
</style>
</head>
<body>
<main class="stage">

  <section class="card card-front" aria-label="Card front">
    <div class="wordmark">
      <span class="wordmark-square"></span>
      <span class="wordmark-text">
        <span class="wordmark-name">Silver Falcon</span>
        <span class="wordmark-sub">Construction Services</span>
      </span>
    </div>
    <div class="band-rule"></div>
    <div class="band">Where Every Great Plan Begins With Solid Groundwork</div>
  </section>

  <section class="card card-back" aria-label="Card back">
    <div class="wordmark">
      <span class="wordmark-square"></span>
      <span class="wordmark-text">
        <span class="wordmark-name">Silver Falcon</span>
        <span class="wordmark-sub">Construction Services</span>
      </span>
    </div>
    <div class="logo-rule"></div>

    <div class="person">
      <p class="person-name">Marissa Vendt</p>
      <p class="person-title">Founder and CEO</p>
    </div>
    <div class="divider"></div>

    <ul class="contacts">
      <li>
        <svg viewBox="0 0 12 12" aria-hidden="true"><rect x="3" y="0.8" width="6" height="10.4" rx="1" fill="none" stroke="#111" stroke-width="1.1"/><circle cx="6" cy="9.4" r="0.6" fill="#111"/></svg>
        720.555.0187
      </li>
      <li>
        <svg viewBox="0 0 12 12" aria-hidden="true"><rect x="0.8" y="2.5" width="10.4" height="7" fill="#111"/><path d="M0.8 2.5 L6 6.6 L11.2 2.5" fill="none" stroke="#fff" stroke-width="0.9"/></svg>
        mvendt@silverfalconbuild.example
      </li>
      <li>
        <svg viewBox="0 0 12 12" aria-hidden="true"><circle cx="6" cy="6" r="5.2" fill="none" stroke="#111" stroke-width="1.1"/><ellipse cx="6" cy="6" rx="2.3" ry="5.2" fill="none" stroke="#111" stroke-width="0.9"/><path d="M0.8 6 H11.2 M1.8 3.3 H10.2 M1.8 8.7 H10.2" stroke="#111" stroke-width="0.8"/></svg>
        www.silverfalconbuild.example
      </li>
    </ul>

    <address class="address">
      4816 Willow Crest Ave,<br>
      Ste 240 Lakewood, CO. 80401
    </address>

    <div class="band-rule"></div>
    <div class="band">Where Every Great Plan Begins With Solid Groundwork</div>
  </section>

</main>
</body>
</html>
```